BUSINESS CARD DESIGN

NAME- TODD MASVERIK
PHONE NUMER - 808- 451-7082
EMAIL- OFFICE@VORLINDE-GRADEWAY.COM
BACK OF CARD- SPEACIALIZES IN LAND CLEARING, FORESTRY MUCLHING AND EXCAVATION

Contact Information for Business Card

NAME- TODD MASVERIK PHONE NUMER - 808- 451-7082 EMAIL- OFFICE@VORLINDE-GRADEWAY.COM BACK OF CARD- SPEACIALIZES IN LAND CLEARING , MUCLHING AND EXCAVATION

```html
<!DOCTYPE html>
<html lang="en">
<head>
<meta charset="utf-8">
<title>Vorlinde Gradeway LLC – Business Card</title>
<link href="https://fonts.googleapis.com/css2?family=Orbitron:wght@500;700;800&display=swap" rel="stylesheet">
<style>
  :root {
    --bg: #3a3a3a;
    --card-black: #000000;
    --card-white: #ffffff;
    --gold: #f5b21f;
    --ink: #111111;
  }
  * { box-sizing: border-box; margin: 0; padding: 0; }
  html, body { width: 1200px; height: 900px; overflow: hidden; }
  body {
    background: var(--bg);
    font-family: "Orbitron", sans-serif;
    position: relative;
  }
  .card {
    position: absolute;
    top: 300px;
    width: 544px;
    height: 314px;
    overflow: hidden;
    box-shadow: 0 6px 18px rgba(0,0,0,.45);
  }
  .card--front { left: 40px; background: var(--card-black); }
  .card--back { left: 616px; background: var(--card-white); }

  .brand-name, .brand-sub, .brand-region,
  .person-name, .contact-email, .contact-phone, .specialty-list { white-space: nowrap; }

  /* Front */
  .brand-front {
    position: absolute;
    top: 66px; left: 0; right: 0;
    text-align: center;
    color: var(--gold);
  }
  .brand-front .mark {
    display: block;
    width: 84px; height: 84px;
    margin: 0 auto 14px;
    border-radius: 50%;
    background: var(--gold);
  }
  .brand-name {
    font-weight: 700;
    letter-spacing: 1px;
    line-height: 1;
  }
  .brand-front .brand-name { font-size: 17px; }
  .brand-sub {
    display: flex; align-items: center; justify-content: center; gap: 8px;
    font-weight: 500;
    letter-spacing: 4px;
    line-height: 1;
  }
  .brand-sub::before, .brand-sub::after {
    content: ""; height: 1.5px; background: currentColor;
  }
  .brand-front .brand-sub { font-size: 10px; margin-top: 5px; }
  .brand-front .brand-sub::before, .brand-front .brand-sub::after { width: 46px; }
  .brand-region { font-weight: 500; letter-spacing: 4px; line-height: 1; }
  .brand-front .brand-region { font-size: 10px; margin-top: 3px; }

  .specialty {
    position: absolute;
    top: 258px; left: 0; right: 0;
    text-align: center;
  }
  .specialty-lead {
    color: var(--card-white);
    font-size: 8px; font-weight: 700; letter-spacing: .5px;
  }
  .specialty-list {
    color: var(--gold);
    font-size: 13px; font-weight: 700; letter-spacing: .6px;
    margin-top: 7px;
  }

  /* Back */
  .brand-back {
    position: absolute;
    top: 34px; left: 34px;
    width: 244px;
    text-align: center;
    color: var(--ink);
  }
  .brand-back .brand-name { font-size: 14px; letter-spacing: .8px; }
  .brand-back .brand-sub { font-size: 10px; margin-top: 5px; }
  .brand-back .brand-sub::before, .brand-back .brand-sub::after { width: 58px; }
  .brand-back .brand-region { font-size: 10px; margin-top: 2px; }

  .hero-art {
    position: absolute;
    top: 30px; left: 292px;
    width: 234px; height: 200px;
  }
  .person {
    position: absolute;
    top: 180px; left: 34px;
    color: var(--ink);
  }
  .person-name { font-size: 17px; font-weight: 700; letter-spacing: 1px; }
  .person-role { font-size: 10px; font-weight: 700; letter-spacing: .5px; margin-top: 6px; }

  .contact-band {
    position: absolute;
    left: 0; right: 0; bottom: 0;
    height: 84px;
    background: var(--card-black);
    padding: 20px 34px 0;
    color: var(--gold);
  }
  .contact-email { font-size: 14px; font-weight: 700; letter-spacing: .6px; }
  .contact-phone { font-size: 25px; font-weight: 800; letter-spacing: 1.5px; margin-top: 4px; }
</style>
</head>
<body>
  <section class="card card--front">
    <div class="brand-front">
      <span class="mark"></span>
      <div class="brand-name">VORLINDE GRADEWAY</div>
      <div class="brand-sub">LLC</div>
      <div class="brand-region">HAWAII</div>
    </div>
    <div class="specialty">
      <div class="specialty-lead">SPEACIALIZES IN</div>
      <div class="specialty-list">LAND CLEARING, MULCHING &amp; EXCAVATION</div>
    </div>
  </section>

  <section class="card card--back">
    <div class="brand-back">
      <div class="brand-name">VORLINDE GRADEWAY</div>
      <div class="brand-sub">LLC</div>
      <div class="brand-region">HAWAII</div>
    </div>

    <svg class="hero-art" viewBox="0 0 234 200" role="img" aria-label="Silhouette of palm trees beside an excavator on the ground">
      <defs>
        <linearGradient id="artFade" x1="0" y1="0" x2="0" y2="1">
          <stop offset="0" stop-color="#ffffff"/>
          <stop offset="1" stop-color="#d9d9d9"/>
        </linearGradient>
      </defs>
      <rect width="234" height="200" fill="url(#artFade)"/>
    </svg>

    <div class="person">
      <div class="person-name">TODD MASVERIK</div>
      <div class="person-role">OWNER</div>
    </div>

    <div class="contact-band">
      <div class="contact-email">OFFICE@VORLINDE-GRADEWAY.COM</div>
      <div class="contact-phone">808-451-7082</div>
    </div>
  </section>
</body>
</html>
```